Ferncrest Anglican Church Christmas Advertising

We need a postcard design for our upcoming Christmas events in Dec 2013

This is an exciting time of year and we want to give lots people in the local community a chance to celebrate Christmas with us

Key events
Songs by the Lake Sat 14th Dec 5.00pm Larkwood Reserve, Dunmore St, Ferncrest (opp church)
Christmas Eve Family Service 6.30pm
Christmas Eve Lessons and Carols 8.30pm
Christmas Day Celebration Service 9.30am

We have a church logo to include. Outline of the church with 2 lines, one green and one yellow line.
The advertising should be fun, punchy and bright colours. Possibly use a line such as Christmas Unwrapped...Jesus is the best present. (this is just an idea)

```html
<!DOCTYPE html>
<html lang="en">
<head>
<meta charset="utf-8">
<title>Ferncrest Anglican Church – Christmas Postcard</title>
<link rel="stylesheet" href="https://fonts.googleapis.com/css2?family=Passion+One:wght@400;700&family=Ubuntu:wght@300;400;500&display=swap">
<style>
  :root {
    --backdrop: #e4e4e4;
    --card-light: #ffffff;
    --card-shade: #d9d9d6;
    --ink: #1c1c1c;
    --ink-soft: #555555;
    --festive-red: #c4161c;
    --festive-red-dark: #7a0d10;
    --box-white: #f1f1ef;
    --box-grey: #b9b9b6;
    --footer-grey: #dcdcdc;
    --map-tone: #e9e6dc;
    --map-road: #e8c64a;
  }
  * { box-sizing: border-box; margin: 0; padding: 0; }
  html, body { width: 1200px; height: 900px; overflow: hidden; }
  body {
    background: var(--backdrop);
    font-family: "Ubuntu", Arial, sans-serif;
    color: var(--ink);
    position: relative;
  }
  .card {
    position: absolute;
    top: 113px;
    width: 489px;
    height: 627px;
    box-shadow: 0 4px 14px rgba(0,0,0,.25);
    overflow: hidden;
  }
  .card-front {
    left: 91px;
    background: radial-gradient(circle at 50% 44%, var(--card-light) 0%, #f4f4f2 38%, var(--card-shade) 100%);
  }
  .card-back {
    left: 633px;
    background: radial-gradient(circle at 50% 40%, var(--card-light) 0%, #f6f6f4 55%, #e2e2df 100%);
  }
  .art { position: absolute; display: block; }

  /* front */
  .front-lid { left: 149px; top: 74px; width: 200px; height: 120px; }
  .front-box { left: 116px; top: 360px; width: 266px; height: 187px; }
  .headline {
    position: absolute;
    left: 0; right: 0; top: 214px;
    text-align: center;
    font-family: "Passion One", Impact, sans-serif;
    font-weight: 700;
    color: var(--festive-red);
    text-shadow: 2px 3px 0 var(--festive-red-dark);
    line-height: 1;
  }
  .headline .line-what { display: block; font-size: 46px; }
  .headline .line-mid { display: block; font-size: 27px; margin-top: 4px; }
  .headline .line-christmas { display: block; font-size: 54px; margin-top: 2px; }

  /* back: identity */
  .identity {
    position: absolute;
    left: 60px; top: 44px;
    display: flex; align-items: center; gap: 20px;
  }
  .identity-mark { width: 34px; height: 34px; background: var(--ink); }
  .identity-name {
    font-size: 34px; font-weight: 400; color: var(--ink); line-height: 1.1;
  }

  /* back: events */
  .events {
    position: absolute;
    left: 14px; top: 186px; width: 310px;
    text-align: center;
  }
  .event { margin-bottom: 16px; }
  .event-title { font-size: 19px; font-weight: 500; line-height: 1.1; }
  .event-detail { font-size: 17px; font-weight: 400; line-height: 1.15; }
  .event-note { font-size: 11px; color: var(--ink-soft); line-height: 1.4; }

  /* back: verse */
  .verse-lid { left: 314px; top: 187px; width: 113px; height: 62px; }
  .verse-box { left: 318px; top: 360px; width: 126px; height: 83px; }
  .verse {
    position: absolute;
    left: 300px; top: 268px; width: 150px;
    text-align: center;
    font-family: "Passion One", Impact, sans-serif;
    color: var(--ink);
    line-height: 1;
  }
  .verse-line { display: block; font-size: 17px; letter-spacing: .3px; }
  .verse-name { display: block; font-size: 32px; margin-top: 2px; }
  .verse-ref { display: block; font-family: "Ubuntu", Arial, sans-serif; font-size: 10px; margin-top: 3px; }

  /* back: footer */
  .footer {
    position: absolute;
    left: 0; bottom: 0; width: 100%; height: 120px;
    background: var(--footer-grey);
  }
  .contact {
    position: absolute;
    left: 0; top: 20px; width: 287px;
    text-align: center;
    font-size: 16px; font-weight: 300; color: #3a3a3a; line-height: 1.3;
  }
  .location-map {
    left: 287px; top: 0; width: 202px; height: 120px;
  }
</style>
</head>
<body>

<section class="card card-front" aria-label="Postcard front">
  <svg class="art front-lid" role="img" aria-label="Gift box lid with red ribbon bow floating open" viewBox="0 0 200 120">
    <defs>
      <linearGradient id="lidTone" x1="0" y1="0" x2="0" y2="1">
        <stop offset="0" stop-color="#c4161c"/>
        <stop offset=".45" stop-color="#e9e9e6"/>
        <stop offset="1" stop-color="#8f8f8c"/>
      </linearGradient>
    </defs>
    <rect width="200" height="120" rx="6" fill="url(#lidTone)" opacity=".85"/>
  </svg>

  <h1 class="headline">
    <span class="line-what">WHAT</span>
    <span class="line-mid">DO YOU WANT FOR</span>
    <span class="line-christmas">CHRISTMAS?</span>
  </h1>

  <svg class="art front-box" role="img" aria-label="Open white gift box with red ribbon" viewBox="0 0 266 187">
    <defs>
      <linearGradient id="boxTone" x1="0" y1="0" x2="1" y2="0">
        <stop offset="0" stop-color="#f3f3f1"/>
        <stop offset=".5" stop-color="#d9d9d6"/>
        <stop offset="1" stop-color="#c9c9c6"/>
      </linearGradient>
    </defs>
    <rect width="266" height="187" rx="6" fill="url(#boxTone)"/>
  </svg>
</section>

<section class="card card-back" aria-label="Postcard back">
  <div class="identity">
    <span class="identity-mark" aria-hidden="true"></span>
    <span class="identity-name">Ferncrest<br>Anglican Church</span>
  </div>

  <div class="events">
    <div class="event">
      <p class="event-title">Songs by the Lake, Sat 14th Dec</p>
      <p class="event-detail">Family Picnic 6.00pm</p>
      <p class="event-detail">Carols @ 7.00pm</p>
      <p class="event-note">Larkwood Reserve, Dunmore St, Ferncrest (opp church)</p>
    </div>
    <div class="event">
      <p class="event-title">Christmas Eve</p>
      <p class="event-detail">Family Service 6.30pm</p>
    </div>
    <div class="event">
      <p class="event-title">Christmas Eve</p>
      <p class="event-detail">Lessons &amp; Carols 9.00pm</p>
    </div>
    <div class="event">
      <p class="event-title">Christmas Day</p>
      <p class="event-detail">Celebration Service 9.00am</p>
    </div>
    <div class="event">
      <p class="event-title">Holiday Club</p>
      <p class="event-detail">Mon 20th - Thur 23rd Jan 2014</p>
      <p class="event-note">Contact us for details and registration</p>
    </div>
  </div>

  <svg class="art verse-lid" role="img" aria-label="Small gift box lid with red bow" viewBox="0 0 113 62">
    <rect width="113" height="62" rx="4" fill="url(#lidTone)" opacity=".85"/>
  </svg>

  <p class="verse">
    <span class="verse-line">THE GIFT OF GOD IS</span>
    <span class="verse-line">ETERNAL LIFE IN</span>
    <span class="verse-name">JESUS</span>
    <span class="verse-ref">ROMANS 6:23</span>
  </p>

  <svg class="art verse-box" role="img" aria-label="Small open white gift box with red ribbon" viewBox="0 0 126 83">
    <rect width="126" height="83" rx="4" fill="url(#boxTone)"/>
  </svg>

  <footer class="footer">
    <address class="contact">
      Cnr Alder &amp;<br>
      Northgate Hwy, Ferncrest<br>
      02 5550 1234;<br>
      www.ferncrestanglican.info
    </address>
    <svg class="art location-map" role="img" aria-label="Street map showing the church location" viewBox="0 0 202 120" preserveAspectRatio="none">
      <defs>
        <linearGradient id="mapTone" x1="0" y1="0" x2="1" y2="1">
          <stop offset="0" stop-color="#efece4"/>
          <stop offset=".6" stop-color="#e9e3c8"/>
          <stop offset="1" stop-color="#e6d79a"/>
        </linearGradient>
      </defs>
      <rect width="202" height="120" fill="url(#mapTone)"/>
    </svg>
  </footer>
</section>

</body>
</html>
```